Hello,
We’re looking for a new WordPress website for Gather Your Light, our company offering unique well-being retreats and workshops.
We currently have a website online (you can consult it : www.gatheryourlight.ch), but we now need to build a new site on WordPress — more flexible, more intuitive to manage, and better aligned with our evolving needs.

What we’re looking for:
A new userfriendly WordPress site, with:
Inspiring, elegant, and modern design
Smooth user experience on desktop and mobile
Innovative design proposals – we want to be inspired !
SEO best practices
Respect of our existing color palette
The final website will need to be set up on our existing hosting provider (details can be shared later)

Pages to Include:
- Home
- Our Story
- Our Stays - with links to 5 individual pages, each describing one of our stays in detail.
- Activities – with potential links to individual descriptive pages
- Agenda
- Our Charter
- The Team
- Contact
- Blog

Required Features:
- Space for photos and videos
- Sections for testimonials and press articles
- Blog/article layout with strong readability
- Easy-to-update backend for future content
- Newsletter sign-up (pop-up and in footer)
- Additional pop-up on/off
- “Request info” buttons
- “Booking request” buttons
- Integration of our 4 pillars - Breathe · Feel · Connect · Experience - in the design (They’re currently in the footer, but we’re open to creative suggestions)

Who we are :
Gather Your Light offers well-being and personal growth stays but with a very different spirit.
We’re not a classic wellness brand. Our approach is professional, joyful, and grounded.
We create spaces where people can take a real break — breathe, slow down, and reconnect with themselves.
During our stays, people are welcomed like friends:
with warmth, respect, and no pressure.
Each program combines practices like breathwork, movement, creativity, coaching, and massages in a relaxed, beautiful setting of the French Alps.
What makes us different:
A friendly and down-to-earth atmosphere
A wide mix of activities.
A mix of inner work and simple pleasures
Private rooms, nourishing food, and shared moments
Time to talk, to laugh, to walk, or just be silent together - and feel free to be yourself
Our guests come to pause.
They leave feeling lighter, aligned, and full of life

```html
<!DOCTYPE html>
<html lang="en">
<head>
<meta charset="utf-8">
<title>Gather Your Light – Well-being stays in the French Alps</title>
<link rel="stylesheet" href="https://fonts.googleapis.com/css2?family=Montserrat:wght@400;500;600;700&family=Pacifico&display=swap">
<style>
:root{
  --blue:#1b3f9b;
  --teal:#5cc4bd;
  --grey:#e5e5e5;
  --ink:#1f1f1f;
  --white:#fff;
  --black:#000;
}
*{box-sizing:border-box;margin:0;padding:0}
html,body{width:1200px;height:4926px;overflow:hidden}
body{position:relative;font-family:"Montserrat",sans-serif;color:var(--ink);background:var(--white)}
.abs{position:absolute}
a{color:inherit;text-decoration:none}
.btn{position:absolute;display:flex;align-items:center;justify-content:center;font-size:11px;font-weight:600;letter-spacing:.08em;text-transform:uppercase}
.btn--teal{background:var(--teal);color:var(--white)}
.btn--outline{border:1.5px solid var(--blue);color:var(--blue);background:var(--white)}
.h2{font-weight:700;font-size:31px;letter-spacing:.02em;text-transform:uppercase}

/* nav */
.site-nav{top:0;left:0;width:1200px;height:67px;background:var(--white)}
.site-nav__link{position:absolute;top:27px;font-size:10.5px;font-weight:500;text-transform:uppercase;color:#333}
.wordmark{position:absolute;left:0;width:1200px;text-align:center;font-weight:700;line-height:1;white-space:nowrap}
.wordmark--header{top:22px;font-size:22px;color:var(--blue)}

/* hero */
.hero{top:67px;left:0;width:1200px;height:591px;background:linear-gradient(160deg,#5f7d3a 0%,#a9b988 40%,#7d9854 70%,#40572a 100%)}
.hero__kicker{left:113px;top:120px;color:var(--white);font-weight:700;font-size:32px;letter-spacing:.04em}
.hero__title{left:113px;top:163px;color:var(--white);font-weight:700;font-size:50px;letter-spacing:.03em;white-space:nowrap}
.hero__text{left:113px;top:229px;width:600px;color:var(--white);font-size:13.5px;line-height:20px}
.hero__play{left:113px;top:316px;display:flex;align-items:center;gap:16px;color:var(--white)}
.hero__play span{font-family:"Pacifico",cursive;font-size:16px}
.hero__panel{left:520px;top:415px;width:680px;height:176px;background:var(--blue)}
.hero__panel p{position:absolute;left:60px;top:40px;width:520px;color:var(--white);font-size:13.5px;line-height:20px}
.hero__panel .btn{left:60px;top:101px;width:136px;height:33px;border:1.5px solid var(--teal);color:var(--teal)}

/* who */
.who{top:658px;left:0;width:1200px;height:589px}
.who__title{left:113px;top:122px}
.who__body{left:113px;top:180px;width:500px;font-size:11.5px;line-height:15.5px;color:#333}
.who__body p{margin-bottom:13px}
.who__photo{left:682px;top:0;width:518px;height:589px;background:linear-gradient(180deg,#6b5a47 0%,#a58a5e 55%,#d8b169 100%)}

/* stays strip */
.stays{top:1247px;left:0;width:1200px;height:175px}
.stays__grey{left:0;top:0;width:682px;height:175px;background:var(--grey)}
.stay{position:absolute;top:42px;width:230px}
.stay h4{font-size:12px;font-weight:700;text-transform:uppercase}
.stay h5{font-size:10px;font-weight:600;margin-top:4px}
.stay p{font-size:10px;line-height:14px;color:#666;margin-top:18px}
.stays__link{left:940px;top:77px;display:flex;align-items:center;gap:28px;font-weight:700;font-size:15px}

.meadow{top:1422px;left:0;width:1200px;height:459px;background:linear-gradient(180deg,#4d7a2f 0%,#b9a824 45%,#e0c21c 60%,#3f6b24 100%)}

/* team */
.team{top:1881px;left:0;width:1200px;height:802px}
.team__grey{left:516px;top:0;width:684px;height:802px;background:var(--grey)}
.team__meet{left:113px;top:86px;display:flex;align-items:center;gap:26px;font-weight:700;font-size:15px}
.team__photo{left:0;top:176px;width:516px;height:626px;background:linear-gradient(180deg,#a9c5e0 0%,#6f8fb3 30%,#cfc7b8 60%,#7b6e5d 100%)}
.team__title{left:589px;top:100px;font-size:30px}
.team__list{left:589px;top:196px;width:501px;list-style:none}
.team__item{border-bottom:1px solid #c6c6c6;height:84px;padding-top:33px}
.team__item:first-child{height:114px;padding-top:0}
.team__item:last-child{border:0}
.team__label{display:flex;align-items:center;gap:11px;font-size:13px;font-weight:600;line-height:16px}
.team__label::before{content:"";width:13px;height:13px;border-radius:50%;background:var(--blue);flex:none}
.team__item--open .team__label::before{background:var(--teal)}
.team__item p{font-size:11px;line-height:19px;color:#555;margin-top:10px}

/* history */
.history{top:2683px;left:0;width:1200px;height:439px;text-align:center}
.history__title{left:0;width:1200px;top:85px}
.history__body{left:206px;top:142px;width:788px;font-size:11.5px;line-height:16px;color:#555}
.history__body p{margin-bottom:16px}
.history .btn{left:532px;top:293px;width:136px;height:32px}

/* testimonials */
.reviews{top:3122px;left:0;width:1200px;height:591px}
.reviews__blue{left:0;top:0;width:682px;height:591px;background:var(--blue)}
.reviews__title{left:113px;top:140px;color:var(--white);line-height:48px}
.reviews__name{left:113px;top:285px;color:var(--white);font-weight:600;font-size:19px}
.reviews__role{left:113px;top:311px;color:#b9c8ee;font-size:11px;font-weight:600}
.reviews__stars{left:113px;top:333px}
.reviews__quote{left:113px;top:362px;width:520px;color:var(--white);font-size:11.5px;line-height:19px}
.dots{display:flex;gap:6px}
.dot{width:9px;height:9px;border-radius:50%;background:#9aa3b8}
.dot--on{background:var(--teal)}
.reviews__photo{left:682px;top:0;width:518px;height:591px;background:linear-gradient(180deg,#7e8f58 0%,#a8b48c 45%,#cbb89e 65%,#6f7f4b 100%)}

/* blogs */
.blogs{top:3713px;left:0;width:1200px;height:627px}
.blogs__title{left:0;width:1200px;top:70px;text-align:center}
.post{position:absolute;top:143px;width:316px}
.post__img{height:211px}
.post h3{margin:22px 10px 0;font-size:12px;font-weight:700;line-height:14px;text-transform:uppercase}
.post p{margin:10px 10px 0;font-size:10.5px;line-height:15px;color:#666}
.post svg{margin:14px 10px 0}
.blogs .dots{position:absolute;left:576px;top:529px}

/* newsletter */
.news{top:4340px;left:0;width:1200px;height:279px;background:var(--grey);text-align:center}
.news__title{left:0;width:1200px;top:62px}
.news__text{left:0;width:1200px;top:118px;font-size:11px;color:#444}
.news__input{left:428px;top:157px;width:262px;height:32px;border:1px solid #999;background:var(--white);font-size:11px;color:#777;text-align:left;padding:9px 16px}
.news .btn{left:692px;top:157px;width:153px;height:32px}

/* footer */
.footer{top:4619px;left:0;width:1200px;height:307px;background:var(--black);color:var(--white);text-align:center}
.wordmark--footer{top:68px;font-size:24px;color:var(--white)}
.footer__nav{left:0;width:1200px;top:149px;display:flex;justify-content:center;gap:28px;font-size:10px;font-weight:500;text-transform:uppercase}
.footer__rule{left:300px;top:180px;width:600px;height:1px;background:#333}
.footer__social{left:0;width:1200px;top:203px;display:flex;justify-content:center;gap:12px}
.footer__social span{width:28px;height:28px;border-radius:50%;background:var(--blue)}
.footer__copy{left:0;width:1200px;top:264px;font-size:9.5px;color:#bbb}
</style>
</head>
<body>

<header class="abs site-nav">
  <a class="site-nav__link" style="left:113px">Our Story</a>
  <a class="site-nav__link" style="left:203px">Our Stays</a>
  <a class="site-nav__link" style="left:289px">Activities</a>
  <a class="site-nav__link" style="left:373px">Agenda</a>
  <div class="wordmark wordmark--header">Gather Your Light</div>
  <a class="site-nav__link" style="left:757px">Our Charter</a>
  <a class="site-nav__link" style="left:862px">The Team</a>
  <a class="site-nav__link" style="left:945px">Blog</a>
  <a class="site-nav__link" style="left:1001px">Contact</a>
  <svg class="abs" style="left:1077px;top:28px" width="11" height="11" viewBox="0 0 11 11" fill="none" stroke="#333" stroke-width="1.3"><circle cx="4.5" cy="4.5" r="3.6"/><path d="M7.2 7.2L10.3 10.3"/></svg>
</header>

<section class="abs hero" role="img" aria-label="Dandelion clocks in a sunny green meadow">
  <div class="abs hero__kicker">WELCOME TO</div>
  <h1 class="abs hero__title">GATHER YOUR LIGHT</h1>
  <p class="abs hero__text">Imagine a space designed to allow for a true break, where every breath counts. Through its retreats,&nbsp; Gather Your Light&nbsp; invites you on an inner and outer journey, a unique experience where each step reconnects you with your vitality and well-being.</p>
  <div class="abs hero__play">
    <svg width="58" height="58" viewBox="0 0 58 58"><circle cx="29" cy="29" r="29" fill="#5cc4bd"/><path d="M23 18L40 29L23 40Z" fill="#fff"/></svg>
    <span>Play Now</span>
  </div>
  <div class="abs hero__panel">
    <p>Take a deep breath&nbsp; and indulge in the luxury of slowing down. Our programs are designed to help each participant reconnect with calm and serenity.</p>
    <a class="btn">Book Now</a>
  </div>
</section>

<section class="abs who">
  <h2 class="abs h2 who__title">Who We Are</h2>
  <div class="abs who__body">
    <p>Gather Your Light offers well-being and personal growth stays but with a very different spirit.</p>
    <p>We’re not a classic wellness brand. Our approach is professional, joyful, and grounded.</p>
    <p>We create spaces where people can take a real break — breathe, slow down, and reconnect with themselves.</p>
    <p>During our stays, people are welcomed like friends:<br>with warmth, respect, and no pressure.</p>
    <p>Each program combines practices like breathwork, movement, creativity, coaching, and massages in a relaxed, beautiful setting of the French Alps.</p>
  </div>
  <a class="btn btn--teal" style="left:113px;top:409px;width:136px;height:32px">Leran More</a>
  <a class="btn btn--outline" style="left:260px;top:409px;width:136px;height:32px">Book Now</a>
  <div class="abs who__photo" role="img" aria-label="Guest seated on cushions in a candle-lit workshop room with fairy lights"></div>
</section>

<section class="abs stays">
  <div class="abs stays__grey"></div>
  <div class="stay" style="left:113px">
    <h4>Instant</h4><h5>A workshop, a time for yourself</h5>
    <p>Sometimes all it takes is a moment to refocus, breathe, and reconnect with yourself.</p>
  </div>
  <div class="stay" style="left:414px">
    <h4>Flight</h4><h5>An Invitation to Spread Your Wings</h5>
    <p>Treat yourself to a week to explore new dimensions of your well-being and open a rewarding chapter in your life.</p>
  </div>
  <a class="abs stays__link">
    <svg width="26" height="12" viewBox="0 0 26 12" fill="none" stroke="#1b3f9b" stroke-width="1.6"><path d="M25 6H2M7 1L2 6L7 11"/></svg>OUR STAYS
  </a>
</section>

<div class="abs meadow" role="img" aria-label="Close-up of yellow dandelion flowers in green grass"></div>

<section class="abs team">
  <div class="abs team__grey"></div>
  <a class="abs team__meet">MEET OUR TEAM
    <svg width="26" height="12" viewBox="0 0 26 12" fill="none" stroke="#1b3f9b" stroke-width="1.6"><path d="M1 6H24M19 1L24 6L19 11"/></svg>
  </a>
  <div class="abs team__photo" role="img" aria-label="Team members at a terrace table overlooking a lake and mountains"></div>
  <h2 class="abs h2 team__title">The Team</h2>
  <ul class="abs team__list">
    <li class="team__item team__item--open"><span class="team__label">The founding team:</span>
      <p>Maëlle and her eventful career; Solène and Amandine with their coaching careers; Loïc with his flamboyant youth and his IT/design support; then Noémie , who laid the first stone.</p></li>
    <li class="team__item"><span class="team__label">Our speakers</span></li>
    <li class="team__item"><span class="team__label">Our team of masseurs</span></li>
    <li class="team__item"><span class="team__label">Our sports team</span></li>
    <li class="team__item"><span class="team__label">Our coaches</span></li>
    <li class="team__item"><span class="team__label">Our sensory experiences</span></li>
  </ul>
</section>

<section class="abs history">
  <h2 class="abs h2 history__title">Our History</h2>
  <div class="abs history__body">
    <p>Gather Your Light is, above all, a story of men and women, a story of encounters and desire, a desire to share, a desire to refocus and a desire to breathe.</p>
    <p>Absorbed in a world that is running out of time, it has become essential to find a little personal space to take precisely the time we are so desperately running after.</p>
    <p>Through our fiduciary activities at GATHER The Horizon and GATHER The Answer, we have been able to observe the growing imbalance in most of our lives and the desire was born to create this bubble of respite in a world that is constantly agitated.</p>
  </div>
  <a class="btn btn--teal">Leran More</a>
</section>

<section class="abs reviews">
  <div class="abs reviews__blue"></div>
  <h2 class="abs h2 reviews__title">What Clients Say<br>About Us</h2>
  <div class="abs reviews__name">MAREN</div>
  <div class="abs reviews__role">Pharmacist</div>
  <svg class="abs reviews__stars" width="112" height="20" viewBox="0 0 112 20" fill="#f5c518">
    <path id="star" d="M9 1l2.4 5.3 5.8.6-4.3 3.9 1.2 5.7L9 13.6 3.9 16.5l1.2-5.7L.8 6.9l5.8-.6z"/>
    <use href="#star" x="23"/><use href="#star" x="46"/><use href="#star" x="69"/><use href="#star" x="92"/>
  </svg>
  <p class="abs reviews__quote">"Lorem ipsum dolor sit amet, consectetur adipiscing elit, sed do eiusmod tempor incididunt ut labore et dolore magna aliqua. Quis ipsum suspendisse ultrices gravida. Risus commodo viverra maecenas accumsan lacus vel facilisis. "</p>
  <div class="abs dots" style="left:566px;top:518px"><span class="dot dot--on"></span><span class="dot"></span><span class="dot"></span></div>
  <div class="abs reviews__photo" role="img" aria-label="Woman stretching outdoors in a park in yoga clothing"></div>
</section>

<section class="abs blogs">
  <h2 class="abs h2 blogs__title">Latest Blogs</h2>
  <article class="post" style="left:113px">
    <div class="post__img" role="img" aria-label="Woman stretching in a bright living room" style="background:linear-gradient(160deg,#e9e4dc,#bfb3a1)"></div>
    <h3>Lorem ipsum dolor sit amet, consectetur adipiscing elit.</h3>
    <p>Lorem ipsum dolor sit amet, consectetur adipiscing elit. Phasellus sed efficitur mi, id auctor nulla. Curabitur vulputate odio in leo blandit, eget viverra dui aliquam.</p>
    <svg width="24" height="12" viewBox="0 0 24 12" fill="none" stroke="#1b3f9b" stroke-width="1.5"><path d="M1 6H22M17 1L22 6L17 11"/></svg>
  </article>
  <article class="post" style="left:443px">
    <div class="post__img" role="img" aria-label="Woman meditating cross-legged on a yoga mat by a window" style="background:linear-gradient(160deg,#cfd8c4,#f1f0ec)"></div>
    <h3>Lorem ipsum dolor sit amet, consectetur adipiscing elit. Phasellus sed efficitur mi, id auctor nulla.</h3>
    <p>Lorem ipsum dolor sit amet, consectetur adipiscing elit. Phasellus sed efficitur mi, id auctor nulla. Curabitur vulputate odio in leo blandit, eget viverra</p>
    <svg width="24" height="12" viewBox="0 0 24 12" fill="none" stroke="#1b3f9b" stroke-width="1.5"><path d="M1 6H22M17 1L22 6L17 11"/></svg>
  </article>
  <article class="post" style="left:772px">
    <div class="post__img" role="img" aria-label="Group yoga class raising arms in a white studio" style="background:linear-gradient(160deg,#e6e6e6,#9d9d9d)"></div>
    <h3>Curabitur vulputate odio in leo blandit, eget viverra dui aliquam.</h3>
    <p>Lorem ipsum dolor sit amet, consectetur adipiscing elit. Phasellus sed efficitur mi, id auctor nulla. Curabitur vulputate odio in leo blandit, eget viverra dui aliquam.</p>
    <svg width="24" height="12" viewBox="0 0 24 12" fill="none" stroke="#1b3f9b" stroke-width="1.5"><path d="M1 6H22M17 1L22 6L17 11"/></svg>
  </article>
  <div class="dots"><span class="dot" style="background:var(--blue)"></span><span class="dot"></span><span class="dot"></span></div>
</section>

<section class="abs news">
  <h2 class="abs h2 news__title">Subsribe to Our Newsletter</h2>
  <p class="abs news__text">Keep up our latest news and events. Subscribe our newsletter</p>
  <div class="abs news__input">Enter Your Email</div>
  <a class="btn btn--teal">Subscribe</a>
</section>

<footer class="abs footer">
  <div class="wordmark wordmark--footer">Gather Your Light</div>
  <nav class="abs footer__nav">
    <a>Our Story</a><a>Our Stays</a><a>Activities</a><a>Agenda</a><a>Our Charter</a><a>The Team</a><a>Contact</a><a>Blog</a>
  </nav>
  <div class="abs footer__rule"></div>
  <div class="abs footer__social" aria-label="Social links"><span></span><span></span><span></span><span></span></div>
  <p class="abs footer__copy">COPYRIGHT © 2025. ALL RIGHTS RESERVED.</p>
</footer>

</body>
</html>
```